fieldscoutingpath.com - Social Media Branding

fieldscoutingpath.com --> Social Media Re-Branding & Graphics
Facebook: @fldscoutpath - Instagram: @fieldscoutingpath - Twitter: @fldscoutpath

Looking to find a good designer to help with my fieldscoutingpath.com social media sites!
- facebook banner
- twitter banner
- instagram template (square and banner size)
- Quote or Information Template
- Committed Template (uniformed) - see the ones I made (& i am no professional) at fieldscoutingpath.com/committed - needs to have fieldscoutingpath.com logo, room for: the committed school and the team the player plays on.

Also willing to pay extra for a graphic that is the "complete package" that detail all of the steps of the recruiting process detailed in fieldscoutingpath.com

Font styles to use
Sans Serif

Colors
ec1f27
fbee3e

```html
<!DOCTYPE html>
<html lang="en">
<head>
<meta charset="utf-8">
<title>fieldscoutingpath.com – Free Recruiting Seminar</title>
<link href="https://fonts.googleapis.com/css2?family=Exo+2:wght@700;800&family=Open+Sans:wght@600;700&display=swap" rel="stylesheet">
<style>
  :root {
    --brand-yellow: #fbee3e;
    --brand-red: #ec1f27;
    --ink: #111111;
    --bg-dark: #151515;
    --bg-mid: #4a4a4a;
    --glow: #ffffff;
    --white: #f4f4f4;
    --player-green: #2f8a5c;
  }
  * { margin: 0; padding: 0; box-sizing: border-box; }
  html, body { width: 1200px; height: 800px; overflow: hidden; background: var(--bg-dark); }
  .poster {
    position: relative;
    width: 1200px;
    height: 800px;
    overflow: hidden;
    font-family: "Open Sans", Arial, sans-serif;
    background:
      radial-gradient(ellipse 420px 300px at 650px 320px, var(--glow) 0%, rgba(220,230,226,0.85) 22%, rgba(120,120,120,0.6) 55%, rgba(21,21,21,0) 100%),
      linear-gradient(160deg, #1a1a1a 0%, var(--bg-mid) 45%, #2a2a2a 70%, #0e0e0e 100%);
  }
  .wave-accent {
    position: absolute;
    pointer-events: none;
  }
  .wave-accent--top { right: 0; top: 0; width: 380px; height: 260px;
    background: radial-gradient(ellipse at 80% 20%, rgba(251,238,62,0.14), rgba(251,238,62,0) 70%); }
  .wave-accent--bottom { right: 0; bottom: 0; width: 700px; height: 330px;
    background: radial-gradient(ellipse at 60% 60%, rgba(251,238,62,0.12), rgba(251,238,62,0) 70%); }
  .wave-accent--left { left: 0; top: 120px; width: 500px; height: 300px;
    background: radial-gradient(ellipse at 40% 50%, rgba(251,238,62,0.1), rgba(251,238,62,0) 70%); }

  .brand {
    position: absolute;
    left: 28px;
    top: 14px;
    display: flex;
    align-items: center;
    gap: 22px;
  }
  .brand__mark {
    width: 110px; height: 110px;
    border-radius: 50%;
    background: var(--brand-yellow);
    flex: none;
  }
  .brand__name {
    font-family: "Open Sans", Arial, sans-serif;
    font-weight: 700;
    font-size: 37px;
    color: var(--white);
    letter-spacing: -0.3px;
    line-height: 1;
  }
  .brand__rule {
    position: absolute;
    left: 175px; top: 89px;
    width: 305px; height: 2px;
    background: var(--brand-red);
  }

  .headline {
    position: absolute;
    left: 318px; top: 142px;
    font-family: "Exo 2", Arial, sans-serif;
    font-weight: 800;
    font-size: 50px;
    letter-spacing: 2px;
    color: var(--brand-yellow);
    text-shadow: 0 2px 4px rgba(0,0,0,0.45);
    white-space: nowrap;
  }

  .player-art {
    position: absolute;
    left: 185px; top: 205px;
    width: 290px; height: 515px;
    background: radial-gradient(ellipse at 45% 40%, rgba(47,138,92,0.75), rgba(47,138,92,0.25) 60%, rgba(47,138,92,0) 100%);
  }

  .audience {
    position: absolute;
    left: 703px; top: 440px;
    width: 405px;
    font-weight: 600;
    font-size: 30px;
    color: var(--brand-red);
    white-space: nowrap;
    letter-spacing: -0.3px;
  }
  .schedule {
    position: absolute;
    left: 703px; top: 498px;
    width: 405px; height: 60px;
    border-radius: 30px;
    background: var(--brand-yellow);
    display: flex;
    align-items: center;
    justify-content: center;
    gap: 34px;
    font-weight: 700;
    font-size: 30px;
    color: var(--ink);
  }

  .site-link {
    position: absolute;
    left: 44px; top: 735px;
    display: flex;
    align-items: center;
    gap: 12px;
    font-weight: 700;
    font-size: 30px;
    color: var(--brand-yellow);
  }
  .site-link__icon { width: 36px; height: 36px; flex: none; }
</style>
</head>
<body>
  <main class="poster">
    <div class="wave-accent wave-accent--top"></div>
    <div class="wave-accent wave-accent--left"></div>
    <div class="wave-accent wave-accent--bottom"></div>

    <header class="brand">
      <span class="brand__mark"></span>
      <span class="brand__name">fieldscoutingpath.com</span>
    </header>
    <div class="brand__rule"></div>

    <h1 class="headline">FREE RECRUITING SEMINAR</h1>

    <div class="player-art" role="img" aria-label="Illustration of a softball batter in a green uniform mid-swing"></div>

    <p class="audience">Players | Parents | Coaches</p>
    <p class="schedule"><span>WEDNESDAY</span><span>7 PM ET</span></p>

    <footer class="site-link">
      <svg class="site-link__icon" viewBox="0 0 36 36" aria-hidden="true" fill="none" stroke="#ec1f27" stroke-width="2.6">
        <circle cx="18" cy="18" r="16"/>
        <ellipse cx="18" cy="18" rx="7" ry="16"/>
        <line x1="2" y1="18" x2="34" y2="18"/>
        <path d="M5 10h26M5 26h26"/>
      </svg>
      <span>www.fieldscoutingpath.com</span>
    </footer>
  </main>
</body>
</html>
```